Real Estate Webpage Design

We have an existing website: verindaleestates.com.au
We focus customised service mainly on Property Management and second-hand property sales.
We are not entirely happy about the current design and layout can stay roughly the same as the back end coding is linked to a CRM system.
We would like to see the design are more reachable to our clients and appearing.
Please check our Website Design Draft for more details.

Industry/Entity Type

Real estate Agency

Number of Pages Required

5+ page

Font styles to use
Sans Serif

Colors

Designer to choose colors to be used in the design.

```html
<!DOCTYPE html>
<html lang="en">
<head>
<meta charset="utf-8">
<title>La Morada – Real Estate</title>
<link rel="stylesheet" href="https://fonts.googleapis.com/css2?family=Open+Sans:wght@600;700&family=Montserrat:wght@400;500;600;700&display=swap">
<style>
:root{
  --gold:#e9bb5b;
  --black:#000;
  --panel:#262626;
  --card:#f7f7f7;
  --ink:#111;
  --muted:#666;
  --white:#fff;
}
*{box-sizing:border-box;margin:0;padding:0}
html,body{width:1200px;height:5021px;overflow:hidden}
body{font-family:"Montserrat",sans-serif;color:var(--ink);background:var(--white);position:relative}
.section{position:absolute;left:0;width:1200px}
.heading{font-family:"Open Sans",sans-serif;font-weight:700;font-size:48px;text-align:center;position:absolute;left:0;width:100%}
.heading span{color:var(--gold)}
.btn{display:flex;align-items:center;justify-content:center;background:var(--gold);color:var(--ink);font-weight:700;font-size:14px;position:absolute}

/* header */
.site-header{top:0;height:82px;background:var(--white)}
.brand{position:absolute;left:104px;top:26px;display:flex;align-items:center;gap:8px;font-weight:600;font-size:18px;color:var(--gold)}
.brand i{width:22px;height:22px;border:2px solid var(--gold);display:block}
.nav{position:absolute;right:103px;top:32px;display:flex;gap:26px;font-size:11px;font-weight:600}
.nav a{color:var(--ink);text-decoration:none}
.nav a.active{color:var(--gold)}

/* hero */
.hero{top:82px;height:593px;background:linear-gradient(180deg,#1c2838 0%,#2b3a4c 40%,#1e4f78 75%,#14385a 100%)}
.hero-title{position:absolute;top:100px;left:0;width:100%;text-align:center;color:var(--white);font-family:"Open Sans",sans-serif;font-weight:700;font-size:62px;line-height:82px}
.hero-title span{color:var(--gold)}
.hero-text{position:absolute;top:278px;left:220px;width:760px;text-align:center;color:var(--white);font-size:17px;line-height:30px}
.hero .btn{left:485px;top:432px;width:228px;height:50px}

/* filter */
.filter{top:675px;height:80px;background:var(--black);display:flex;padding-left:108px}
.filter div{width:158px;height:64px;margin-top:8px;margin-right:7px;display:flex;align-items:center;justify-content:center;color:var(--white);font-size:14px;font-weight:600}
.filter .on{background:var(--gold);color:var(--ink)}

/* listings */
.listings{top:755px;height:645px}
.listing{position:absolute;top:94px;width:230px;height:456px;background:var(--card);text-align:center}
.photo{display:block;width:100%}
.listing .photo{height:203px}
.listing h3{font-size:15px;font-weight:700;margin-top:22px}
.listing .addr{font-size:10px;margin-top:10px}
.feats{display:flex;justify-content:center;gap:30px;margin-top:18px;font-size:11px}
.feats span{display:flex;align-items:center;gap:6px}
.price{font-size:11px;font-weight:600;margin-top:20px}
.insp{font-size:14px;font-weight:700;margin-top:12px}
.time{font-size:10px;margin-top:12px}
.bar{position:absolute;bottom:0;left:0;width:100%;height:34px;background:var(--black);display:flex;align-items:center;justify-content:center;gap:10px}

/* about */
.about{top:1400px;height:970px;background:var(--black)}
.about .heading{top:60px;color:var(--white)}
.about-frame{position:absolute;left:78px;top:192px;width:540px;height:500px;border:1px solid var(--gold)}
.about .photo{position:absolute;left:97px;top:212px;width:540px;height:500px}
.about-box{position:absolute;left:563px;top:282px;width:538px;height:576px;background:var(--panel);color:var(--white);text-align:center;padding:66px 44px 0;font-size:17px;line-height:30px}
.about-box-frame{position:absolute;left:580px;top:298px;width:540px;height:576px;border:1px solid var(--gold);border-left:none;border-top-color:var(--gold)}
.about-box .btn{left:163px;top:476px;width:228px;height:52px}

/* team */
.team{top:2370px;height:680px}
.team .heading{top:98px}
.member{position:absolute;top:223px;width:330px}
.member .photo{width:156px;height:156px;border-radius:8px}
.member h4{font-size:18px;font-weight:600;margin-top:36px}
.member .role{font-size:14px;color:var(--muted);margin-top:12px}
.contact{display:flex;align-items:center;gap:18px;font-size:11px;margin-top:14px}
.arrow{position:absolute}

/* testimonials */
.testimonials{top:3050px;height:640px;background:var(--black)}
.testimonials .heading{top:100px;color:var(--white)}
.quote{position:absolute;top:225px;width:474px;height:316px;background:var(--panel);color:var(--white);padding:36px 34px}
.quote-frame{position:absolute;top:240px;width:474px;height:316px;border:1px solid var(--gold);border-left:none}
.who{display:flex;gap:32px;align-items:flex-start}
.avatar{width:62px;height:62px}
.who h5{font-size:17px;font-weight:600;margin-top:4px}
.who p{font-size:14px;color:#bbb;margin-top:14px}
.quote .body{font-size:17px;line-height:30px;margin-top:34px}
.meta{display:flex;align-items:center;gap:32px;margin-top:26px;font-size:12px}
.stars{color:var(--gold);font-size:17px;letter-spacing:2px}

/* blog */
.blog{top:3690px;height:840px}
.blog .heading{top:104px}
.post{position:absolute;top:235px;width:230px;height:505px;background:var(--card);text-align:center}
.post .photo{height:203px}
.post .meta-row{display:flex;justify-content:space-between;padding:0 18px 0 16px;font-size:12px;margin-top:25px}
.post h6{font-size:14px;font-weight:700;line-height:20px;margin-top:32px;padding:0 22px}
.post .excerpt{font-size:10px;line-height:17px;margin-top:14px;padding:0 20px}
.post .more{color:var(--gold);font-size:13px;font-weight:600;margin-top:32px}

/* footer */
.footer{top:4530px;height:491px;background:var(--black);color:var(--white)}
.footer h4{position:absolute;top:100px;font-family:"Open Sans",sans-serif;font-size:22px;font-weight:700}
.footer .about-text{position:absolute;left:100px;top:162px;width:160px;font-size:14px;line-height:21px}
.links{position:absolute;left:293px;top:160px;font-size:14px;line-height:31px}
.info{position:absolute;left:467px;top:168px;font-size:15px}
.info div{display:flex;align-items:center;gap:20px;margin-bottom:20px}
.dot{width:30px;height:30px;border-radius:50%;background:var(--gold);display:flex;align-items:center;justify-content:center}
.sub{position:absolute;left:770px;top:152px;display:flex}
.sub .field{width:226px;height:64px;background:var(--white);color:#555;font-size:11px;padding:25px 0 0 26px}
.sub .send{width:82px;height:64px;background:var(--gold);display:flex;align-items:center;justify-content:center}
.social{position:absolute;left:770px;top:256px;display:flex;gap:20px}
.social i{display:block;width:30px;height:30px;border-radius:50%;background:var(--gold)}
.copy{position:absolute;left:0;top:470px;width:100%;text-align:center;font-size:10px;color:#ccc}
</style>
</head>
<body>

<header class="section site-header">
  <div class="brand"><i></i>La Morada</div>
  <nav class="nav">
    <a class="active" href="#">Home</a><a href="#">About Us</a><a href="#">Leasing</a><a href="#">Buy</a><a href="#">Sell</a><a href="#">Our Team</a><a href="#">Blog</a><a href="#">Contact Us</a>
  </nav>
</header>

<section class="section hero" role="img" aria-label="Modern villa at dusk with lit pool">
  <h1 class="hero-title">La <span>Morada</span> – Spanish for<br><span>“the home”</span></h1>
  <p class="hero-text">La Morada in Spanish means “the home, the house”, buying a property is one of the most expensive expenses and important assets for people. La Morada is a real estate company located in Gungahlin, Canberra.</p>
  <a class="btn">Contact Us</a>
</section>

<nav class="section filter">
  <div class="on">All</div><div>For Sale</div><div>For Lease</div><div>Open Times</div><div>Sold</div><div>Lease</div>
</nav>

<section class="section listings">
  <svg width="0" height="0" style="position:absolute">
    <defs>
      <g id="bed"><rect x="1" y="3" width="14" height="8" fill="none" stroke="#e9bb5b" stroke-width="1.4"/><line x1="1" y1="7" x2="15" y2="7" stroke="#e9bb5b" stroke-width="1.4"/></g>
      <g id="bath"><path d="M1 8h14v3H1zM3 8V3h3" fill="none" stroke="#e9bb5b" stroke-width="1.4"/></g>
      <g id="car"><path d="M2 10V7l2-4h8l2 4v3z" fill="none" stroke="#e9bb5b" stroke-width="1.4"/><circle cx="5" cy="10" r="1.3" fill="#e9bb5b"/><circle cx="11" cy="10" r="1.3" fill="#e9bb5b"/></g>
      <g id="tools"><circle cx="8" cy="8" r="6" fill="none" stroke="#e9bb5b" stroke-width="1.5"/><path d="M8 4v4h3" stroke="#e9bb5b" stroke-width="1.5" fill="none"/>
        <g transform="translate(22 0)" fill="#e9bb5b"><rect x="2" y="2" width="4" height="4"/><rect x="10" y="2" width="4" height="4"/><rect x="2" y="10" width="4" height="4"/><rect x="10" y="10" width="4" height="4"/></g>
        <g transform="translate(44 0)"><rect x="1" y="3" width="14" height="10" fill="none" stroke="#e9bb5b" stroke-width="1.5"/><path d="M1 3l7 6 7-6" fill="none" stroke="#e9bb5b" stroke-width="1.5"/></g>
        <path transform="translate(66 0)" d="M8 1l2.2 4.6 5 .6-3.7 3.4 1 5L8 12.2 3.5 14.6l1-5L.8 6.2l5-.6z" fill="#e9bb5b"/></g>
    </defs>
  </svg>

  <article class="listing" style="left:101px">
    <div class="photo" role="img" aria-label="Timber resort house with poolside loungers" style="background:linear-gradient(160deg,#6b3a22,#a8653a 55%,#c9a070)"></div>
    <h3>GUNGAHLIN</h3><p class="addr">Level 5/71/1 Harlow Crest Avenue</p>
    <div class="feats"><span><svg width="16" height="14"><use href="#bed"/></svg>2</span><span><svg width="16" height="14"><use href="#bath"/></svg>2</span><span><svg width="16" height="14"><use href="#car"/></svg>2</span></div>
    <p class="price">$500,000+</p><p class="insp">Next Inspection:</p><p class="time">Sat 21st May 09:40 AM - 10:00 AM</p>
    <div class="bar"><svg width="84" height="16"><use href="#tools"/></svg></div>
  </article>
  <article class="listing" style="left:357px">
    <div class="photo" role="img" aria-label="Apartment courtyard with palms" style="background:linear-gradient(160deg,#d7dde0,#7f9a86 55%,#3f5c45)"></div>
    <h3>BELCONNEN</h3><p class="addr">172/54 Marden Street Belconnen</p>
    <div class="feats"><span><svg width="16" height="14"><use href="#bed"/></svg>2</span><span><svg width="16" height="14"><use href="#bath"/></svg>2</span><span><svg width="16" height="14"><use href="#car"/></svg>2</span></div>
    <p class="price">$500,000+</p><p class="insp">Next Inspection:</p><p class="time">Sat 21st May 09:40 AM - 10:00 AM</p>
    <div class="bar"><svg width="84" height="16"><use href="#tools"/></svg></div>
  </article>
  <article class="listing" style="left:613px">
    <div class="photo" role="img" aria-label="Villa with infinity pool at night" style="background:linear-gradient(180deg,#0f2a66,#1f4fa8 60%,#2a7ad0)"></div>
    <h3>GUNGAHLIN</h3><p class="addr">Level 5/71/1 Harlow Crest Avenue</p>
    <div class="feats"><span><svg width="16" height="14"><use href="#bed"/></svg>2</span><span><svg width="16" height="14"><use href="#bath"/></svg>2</span><span><svg width="16" height="14"><use href="#car"/></svg>2</span></div>
    <p class="price">$500,000+</p><p class="insp">Next Inspection:</p><p class="time">Sat 21st May 09:40 AM - 10:00 AM</p>
    <div class="bar"><svg width="84" height="16"><use href="#tools"/></svg></div>
  </article>
  <article class="listing" style="left:869px">
    <div class="photo" role="img" aria-label="Hotel pool with umbrellas" style="background:linear-gradient(180deg,#8fbde6,#cfd8d4 45%,#2f8fd6 75%,#c88a4a)"></div>
    <h3>GUNGAHLIN</h3><p class="addr">Level 5/71/1 Harlow Crest Avenue</p>
    <div class="feats"><span><svg width="16" height="14"><use href="#bed"/></svg>2</span><span><svg width="16" height="14"><use href="#bath"/></svg>2</span><span><svg width="16" height="14"><use href="#car"/></svg>2</span></div>
    <p class="price">$500,000+</p><p class="insp">Next Inspection:</p><p class="time">Sat 21st May 09:40 AM - 10:00 AM</p>
    <div class="bar"><svg width="84" height="16"><use href="#tools"/></svg></div>
  </article>
</section>

<section class="section about">
  <h2 class="heading">About <span>Us</span></h2>
  <div class="about-frame"></div>
  <div class="photo" role="img" aria-label="Bright kitchen with island and bar stools" style="background:linear-gradient(180deg,#f2f1ee,#e6e3dd 55%,#c9a27a 80%,#b7895c)"></div>
  <div class="about-box-frame"></div>
  <div class="about-box">
    <p>La Morada in Spanish means “the home, the house”, buying a property is one of the most expensive expenses and important assets for people. La Morada is a real estate company located in Gungahlin, Canberra.<br>Being a portfolio sales agent and property manager, coupled with our high-profile international real estate experience, La Morada is considered a market leader on the cutting edge with deep industry knowledge, ranging from landlord-tenant relationships, residential purchases.</p>
    <a class="btn">Read More</a>
  </div>
</section>

<section class="section team">
  <h2 class="heading">Our <span>Team</span></h2>
  <svg class="arrow" style="left:46px;top:388px" width="14" height="18"><path d="M10 2L3 9l7 7" fill="none" stroke="#111" stroke-width="2"/></svg>
  <svg class="arrow" style="left:1140px;top:388px" width="14" height="18"><path d="M4 2l7 7-7 7" fill="none" stroke="#111" stroke-width="2"/></svg>
  <svg width="0" height="0" style="position:absolute"><defs>
    <path id="ph" d="M3 2h4l1.5 4-2 1.5a9 9 0 004 4L12 9.5l4 1.5v4a2 2 0 01-2 2A13 13 0 011 4a2 2 0 012-2z" fill="#111"/>
    <g id="ml"><rect x="1" y="3" width="15" height="11" fill="none" stroke="#111" stroke-width="1.6"/><path d="M1 3l7.5 6L16 3" fill="none" stroke="#111" stroke-width="1.6"/></g>
    <g id="mb"><rect x="4" y="1" width="9" height="16" rx="1.5" fill="none" stroke="#111" stroke-width="1.8"/><rect x="7" y="13" width="3" height="1.6" fill="#111"/></g>
  </defs></svg>
  <div class="member" style="left:101px">
    <div class="photo" role="img" aria-label="Portrait of principal" style="background:linear-gradient(160deg,#dfe3e8,#8a94a0)"></div>
    <h4>Wei Tan</h4><p class="role">Principal</p>
    <div class="contact"><svg width="17" height="18"><use href="#ph"/></svg>+61 6100 0000</div>
    <div class="contact"><svg width="17" height="18"><use href="#ml"/></svg>0400 000 000</div>
    <div class="contact"><svg width="17" height="18"><use href="#mb"/></svg>wtan@verindaleestates.com.au</div>
  </div>
  <div class="member" style="left:476px">
    <div class="photo" role="img" aria-label="Portrait of business relationship manager" style="background:linear-gradient(160deg,#c9c3bb,#6a5648)"></div>
    <h4>Mira Chen</h4><p class="role">Business Relationship manager</p>
    <div class="contact"><svg width="17" height="18"><use href="#ph"/></svg>+61 6100 0000</div>
    <div class="contact"><svg width="17" height="18"><use href="#ml"/></svg>0400 000 000</div>
    <div class="contact"><svg width="17" height="18"><use href="#mb"/></svg>wtan@verindaleestates.com.au</div>
  </div>
  <div class="member" style="left:850px">
    <div class="photo" role="img" aria-label="Portrait of property manager" style="background:linear-gradient(160deg,#9aa77a,#5d6e42)"></div>
    <h4>Lena Ruiz</h4><p class="role">Property Manager</p>
    <div class="contact"><svg width="17" height="18"><use href="#ph"/></svg>+61 6100 0000</div>
    <div class="contact"><svg width="17" height="18"><use href="#ml"/></svg>0400 000 000</div>
    <div class="contact"><svg width="17" height="18"><use href="#mb"/></svg>wtan@verindaleestates.com.au</div>
  </div>
</section>

<section class="section testimonials">
  <h2 class="heading">Client’s <span>Testimonials</span></h2>
  <svg class="arrow" style="left:38px;top:382px" width="14" height="18"><path d="M10 2L3 9l7 7" fill="none" stroke="#fff" stroke-width="2"/></svg>
  <svg class="arrow" style="left:1133px;top:382px" width="14" height="18"><path d="M4 2l7 7-7 7" fill="none" stroke="#fff" stroke-width="2"/></svg>
  <div class="quote-frame" style="left:120px"></div>
  <div class="quote" style="left:106px">
    <div class="who"><div class="avatar" role="img" aria-label="Client portrait" style="background:linear-gradient(160deg,#c8ccd0,#7a8088)"></div><div><h5>Abcdef</h5><p>Doctor</p></div></div>
    <p class="body">Lorem ipsum dolor sit amet, consectetur adipiscing elit. Amet, velit adipiscing id netus sed elit scelerisque.</p>
    <div class="meta"><span>23 April - 8:13 am</span><span class="stars">★★★★★</span></div>
  </div>
  <div class="quote-frame" style="left:620px"></div>
  <div class="quote" style="left:606px">
    <div class="who"><div class="avatar" role="img" aria-label="Client portrait" style="background:linear-gradient(160deg,#c8ccd0,#7a8088)"></div><div><h5>Abdetr</h5><p>Teacher</p></div></div>
    <p class="body">Lorem ipsum dolor sit amet, consectetur adipiscing elit. Amet, velit adipiscing id netus sed elit scelerisque.</p>
    <div class="meta"><span>23 April - 8:13 am</span><span class="stars">★★★★★</span></div>
  </div>
</section>

<section class="section blog">
  <h2 class="heading">Our <span>Blog</span></h2>
  <svg class="arrow" style="left:46px;top:480px" width="14" height="18"><path d="M10 2L3 9l7 7" fill="none" stroke="#111" stroke-width="2"/></svg>
  <svg class="arrow" style="left:1140px;top:480px" width="14" height="18"><path d="M4 2l7 7-7 7" fill="none" stroke="#111" stroke-width="2"/></svg>
  <article class="post" style="left:101px">
    <div class="photo" role="img" aria-label="Family reading together on a sofa" style="background:linear-gradient(160deg,#8a7260,#4e3f36)"></div>
    <div class="meta-row"><span>ABDXFD</span><span>28 Mar,21- 8:13</span></div>
    <h6>Lorem ipsum dolor sit amet, consectetur adipiscing elit.</h6>
    <p class="excerpt">Lorem ipsum dolor sit amet, consectetur adipiscing elit. Tristique sapien pretium at vitae eleifend morbi urna morbi ultrices.</p>
    <p class="more">READ MORE</p>
  </article>
  <article class="post" style="left:357px">
    <div class="photo" role="img" aria-label="Woman relaxing at home with a laptop" style="background:linear-gradient(160deg,#d6d0c8,#9c8f84)"></div>
    <div class="meta-row"><span>ABDXFD</span><span>28 Mar,21- 8:13</span></div>
    <h6>Lorem ipsum dolor sit amet, consectetur adipiscing elit.</h6>
    <p class="excerpt">Lorem ipsum dolor sit amet, consectetur adipiscing elit. Tristique sapien pretium at vitae eleifend morbi urna morbi ultrices.</p>
    <p class="more">READ MORE</p>
  </article>
  <article class="post" style="left:613px">
    <div class="photo" role="img" aria-label="Modern office lobby with warm ceiling lights" style="background:linear-gradient(180deg,#c8944e,#e8d8b8 50%,#2f7f86)"></div>
    <div class="meta-row"><span>ABDXFD</span><span>28 Mar,21- 8:13</span></div>
    <h6>Lorem ipsum dolor sit amet, consectetur adipiscing elit.</h6>
    <p class="excerpt">Lorem ipsum dolor sit amet, consectetur adipiscing elit. Tristique sapien pretium at vitae eleifend morbi urna morbi ultrices.</p>
    <p class="more">READ MORE</p>
  </article>
  <article class="post" style="left:869px">
    <div class="photo" role="img" aria-label="Father hugging his child" style="background:linear-gradient(160deg,#4a4a4a,#a07e66)"></div>
    <div class="meta-row"><span>ABDXFD</span><span>28 Mar,21- 8:13</span></div>
    <h6>Lorem ipsum dolor sit amet, consectetur adipiscing elit.</h6>
    <p class="excerpt">Lorem ipsum dolor sit amet, consectetur adipiscing elit. Tristique sapien pretium at vitae eleifend morbi urna morbi ultrices.</p>
    <p class="more">READ MORE</p>
  </article>
</section>

<footer class="section footer">
  <h4 style="left:100px">La Morada</h4>
  <p class="about-text">Lorem ipsum dolor sit amet, consectetur adipiscing elit. Tristique sapien pretium at vitae eleifend morbi urna morbi ultrices.</p>
  <h4 style="left:293px">Quick Links</h4>
  <div class="links">Home<br>About Us<br>Leasing<br>Buy<br>Sell<br>Our Team<br>Blog<br>Contact Us</div>
  <h4 style="left:467px">Contact Info</h4>
  <div class="info">
    <div><span class="dot"><svg width="14" height="14" viewBox="0 0 18 18"><path d="M3 2h4l1.5 4-2 1.5a9 9 0 004 4L12 9.5l4 1.5v4a2 2 0 01-2 2A13 13 0 011 4a2 2 0 012-2z" fill="#000"/></svg></span>000.000.0000</div>
    <div><span class="dot"><svg width="12" height="16" viewBox="0 0 12 16"><path d="M6 1a5 5 0 015 5c0 4-5 9-5 9S1 10 1 6a5 5 0 015-5z" fill="#000"/><circle cx="6" cy="6" r="2" fill="#e9bb5b"/></svg></span>44 Placeholder Road, Gungahlin</div>
    <div><span class="dot"><svg width="14" height="12" viewBox="0 0 16 13"><rect x="1" y="1" width="14" height="11" fill="none" stroke="#000" stroke-width="1.6"/><path d="M1 1l7 6 7-6" fill="none" stroke="#000" stroke-width="1.6"/></svg></span>hello@verindaleestates.com.au</div>
  </div>
  <h4 style="left:770px">Newsletter</h4>
  <div class="sub"><div class="field">Email</div><div class="send"><svg width="24" height="24" viewBox="0 0 24 24"><path d="M2 11L22 2l-9 20-2-9z" fill="none" stroke="#fff" stroke-width="1.6"/></svg></div></div>
  <div class="social"><i></i><i></i><i></i></div>
  <p class="copy">© 2022 Real estate. ALL RIGHTS RESERVED</p>
</footer>

</body>
</html>
```